VPN Tech Comparison site. Clean and professional looking.

WORDPRESS

We need a website for "NetSafeHub" - A comparison website, news and article site.

We need a website that covers three main from top to bottom.

- Logo
- Menu underneath

- 5 Best of with a table of comparable features

then two columns, left column bigger, right column smaller

Right column to contain latest blog posts with thumbnails all the way down the same length as the left column.

Left column :

Separate section with each "Best for" in a separate section within.

- Best For Device ...

- Best for Country...

- Best for Features

Separate section with each "Latest" in a separate section within.

- Latest News

- Latest Reviews

- Latest Guides

- Latest Articles

Quite like the layout of http://www.trovandi.com/ so something along those lines, although not exactly and less graphically intense.

Target Market(s)

20-60 age range. Mostly male with some female.

Beginner friendly looking.

Industry/Entity Type

Information Technology

Number of Pages Required

2 page

Font styles to use
Sans Serif

Colors
32a6d6
33b8a4

Requirements
Must have
• 1 main page as described in the description.
• 1 blog post page with latest articles in a right side column.
Nice to have
• Easily readable font of a semi-big size for blog posts.
• Not overly graphical.

```html
<!DOCTYPE html>
<html lang="en">
<head>
<meta charset="utf-8">
<title>NetSafeHub</title>
<link href="https://fonts.googleapis.com/css2?family=Open+Sans:wght@400;600&family=Raleway:wght@500;600&display=swap" rel="stylesheet">
<style>
:root{
  --blue:#32a6d6;
  --teal:#33b8a4;
  --teal-dark:#1e957f;
  --nav-top:#41c4ac;
  --nav-bottom:#25a28c;
  --ink:#333;
  --muted:#6a6a6a;
  --header-top:#f7f7f7;
  --header-bottom:#e9e9e9;
  --footer:#e4e4e4;
  --rule:#d6d6d6;
}
*{margin:0;padding:0;box-sizing:border-box}
html,body{width:1200px;height:2296px;overflow:hidden;background:#fff}
body{position:relative;font-family:"Open Sans",Arial,sans-serif;color:var(--ink)}
.abs{position:absolute}

/* header */
.site-header{position:absolute;left:0;top:0;width:1200px;height:112px;background:linear-gradient(var(--header-top),var(--header-bottom));border-bottom:1px solid #dcdcdc}
.brand{position:absolute;left:0;width:1200px;top:28px;text-align:center;font-family:"Raleway",sans-serif;font-weight:600;font-size:38px;color:#222;letter-spacing:.5px}
.search{position:absolute;left:794px;top:53px;width:192px;height:27px;border:1px solid #c9c9c9;border-radius:14px;background:#fff;font-size:10px;color:#999;padding:6px 0 0 14px}
.search svg{position:absolute;right:9px;top:6px}

.main-nav{position:absolute;left:202px;top:92px;width:796px;height:46px;background:linear-gradient(var(--nav-top),var(--nav-bottom));display:flex}
.main-nav a{font-family:"Raleway",sans-serif;font-weight:600;font-size:14.5px;color:#fff;text-decoration:none;display:flex;align-items:center;justify-content:center;border-right:1px solid rgba(255,255,255,.22);flex:1 1 auto}
.main-nav a.active{background:var(--teal-dark)}

/* hero */
.photo{position:absolute}
.hero-main{left:202px;top:148px;width:439px;height:285px;background:linear-gradient(#5e5c5a 0%,#8a7868 25%,#3b4656 55%,#1f2633 100%)}
.hero-title{position:absolute;left:217px;top:370px;font-family:"Raleway",sans-serif;font-weight:600;font-size:21px;color:#fff;letter-spacing:.5px}
.hero-sub{position:absolute;left:217px;top:401px;font-family:"Raleway",sans-serif;font-weight:500;font-size:13px;color:#fff}
.hero-thumb{width:172px;height:140px}
.hero-thumb::after{content:"";position:absolute;inset:7px;border:1px solid rgba(255,255,255,.55)}
.thumb-caption{position:absolute;font-size:14.5px;color:#fff;line-height:1.2}
.thumb-caption small{display:block;font-size:11px}

/* sections */
.section-tab{position:absolute;height:34px;border-bottom:2px solid var(--c)}
.section-tab span{display:block;height:32px;width:180px;background:var(--c);color:#fff;font-family:"Raleway",sans-serif;font-weight:600;font-size:13px;line-height:32px;padding-left:16px;clip-path:polygon(0 0,86% 0,100% 100%,0 100%)}
.tab-blue{--c:var(--blue)}
.tab-teal{--c:var(--teal)}

.card{position:absolute}
.card .photo{position:relative;display:block}
.card h3{font-weight:400;font-size:13px;color:#222;margin-top:13px;line-height:1.3}
.card p{font-size:9.4px;color:var(--muted);line-height:17px;margin-top:3px}
.read-more{display:block;font-size:10px;color:#222;margin-top:3px;letter-spacing:.3px}
.card h4{font-weight:400;font-size:12px;color:var(--teal);margin-top:8px}
.card time{display:block;font-size:10px;color:#222;margin-top:4px;letter-spacing:.3px}

.feature-row{position:absolute;display:flex;gap:18px}
.feature-row h3{margin-top:2px}

.post h4{font-size:13px;margin-top:10px}
.post p{font-size:9.4px;line-height:17px;margin-top:5px}
.post time{font-size:9.5px;margin-top:5px}

/* footer */
.site-footer{position:absolute;left:0;top:2183px;width:1200px;height:113px;background:var(--footer);border-top:1px solid #d2d2d2}
.footer-nav{position:absolute;left:200px;top:30px;display:flex;gap:24px}
.footer-nav a{font-size:11px;color:#333;text-decoration:none}
.copyright{position:absolute;left:200px;top:60px;font-size:10px;color:#888}
.social{position:absolute;left:868px;top:24px;display:flex;gap:4px}
.social span{width:30px;height:30px;border:1.5px solid #555;border-radius:50%}
</style>
</head>
<body>

<header class="site-header">
  <div class="brand">NetSafeHub</div>
  <div class="search">Search here
    <svg width="14" height="14" viewBox="0 0 14 14"><circle cx="6" cy="6" r="4.3" fill="none" stroke="#888" stroke-width="1.6"/><line x1="9.2" y1="9.2" x2="13" y2="13" stroke="#888" stroke-width="1.8"/></svg>
  </div>
</header>

<nav class="main-nav">
  <a class="active" href="#" style="flex:0 0 83px">HOME</a>
  <a href="#">ABOUT</a><a href="#">ARTICLES</a><a href="#">NEWS</a><a href="#">FEATURES</a><a href="#">DEVICE</a><a href="#">REVIEWS</a><a href="#">GUIDES</a><a href="#" style="border-right:0">CONTACT</a>
</nav>

<!-- hero slider -->
<div class="photo hero-main" role="img" aria-label="City skyline at dusk seen from above"></div>
<svg class="abs" style="left:210px;top:262px" width="20" height="46" viewBox="0 0 20 46"><polyline points="17,2 3,23 17,44" fill="none" stroke="#fff" stroke-width="2"/></svg>
<svg class="abs" style="left:610px;top:262px" width="20" height="46" viewBox="0 0 20 46"><polyline points="3,2 17,23 3,44" fill="none" stroke="#fff" stroke-width="2"/></svg>
<div class="hero-title">PELLENTESQUE FAUCIBUS</div>
<div class="hero-sub">CURABITUR IACULIS TEMPUS EROS CURABITUR</div>

<div class="photo hero-thumb" style="left:647px;top:148px;background:linear-gradient(135deg,#9a9a9a,#4a4a4a)" role="img" aria-label="Business person checking a wristwatch"></div>
<div class="thumb-caption" style="left:668px;top:237px">Morbi diam mauris<small>viverra in gravida eu</small></div>
<div class="photo hero-thumb" style="left:826px;top:148px;background:linear-gradient(135deg,#b8ad98,#6d6452)" role="img" aria-label="Office towers in warm light"></div>
<div class="thumb-caption" style="left:840px;top:237px">Nullam enim leo ege<small>viverra in gravida eu</small></div>
<div class="photo hero-thumb" style="left:647px;top:294px;background:linear-gradient(135deg,#3c4f6e,#1a2236)" role="img" aria-label="Team meeting around a desk"></div>
<div class="thumb-caption" style="left:664px;top:382px">Etiam eu urna Sed<small>viverra in gravida eu</small></div>
<div class="photo hero-thumb" style="left:826px;top:294px;background:linear-gradient(135deg,#8c8a88,#3d3a38)" role="img" aria-label="Two colleagues looking at a screen"></div>
<div class="thumb-caption" style="left:838px;top:382px">Suspendisse quam leo<small>viverra in gravida eu</small></div>

<!-- left column -->
<div class="section-tab tab-blue" style="left:199px;top:466px;width:514px"><span>BEST FOR DEVICE</span></div>
<article class="card" style="left:202px;top:514px;width:248px">
  <div class="photo" style="height:146px;background:linear-gradient(135deg,#a4845f,#3d4d5c)" role="img" aria-label="Desk with glasses, tablet and paperwork"></div>
  <h3>Etiam eu urna Sed porta Suspendisse</h3>
  <p>consectetuer adipiscing elit Nam cursus Morbi ut mi Nullam enim leo egestas id condimentum at</p>
  <span class="read-more">READ MORE</span>
</article>
<article class="card" style="left:467px;top:514px;width:248px">
  <div class="photo" style="height:146px;background:linear-gradient(135deg,#e9ecef,#9fb3c8)" role="img" aria-label="Woman relaxing with a laptop"></div>
  <h3>Pellentesque rutrum males</h3>
  <p>consectetuer adipiscing elit Nam cursus Morbi ut mi Nullam enim leo egestas id condimentum at</p>
  <span class="read-more">READ MORE</span>
</article>

<div class="section-tab tab-teal" style="left:199px;top:774px;width:514px"><span>BEST FOR COUNTRY</span></div>
<article class="card" style="left:205px;top:823px;width:248px">
  <div class="photo" style="height:146px;background:linear-gradient(135deg,#f2eee8,#6fc2cf)" role="img" aria-label="Smiling woman holding a tablet"></div>
  <h3>Etiam eu urna Sed porta Suspendisse</h3>
  <p>consectetuer adipiscing elit Nam cursus Morbi ut mi Nullam enim leo egestas id condimentum at</p>
  <span class="read-more">READ MORE</span>
</article>
<article class="card" style="left:470px;top:823px;width:248px">
  <div class="photo" style="height:146px;background:linear-gradient(135deg,#f4f6f8,#b9c3cc)" role="img" aria-label="Group meeting in a bright office"></div>
  <h3>Pellentesque rutrum males</h3>
  <p>consectetuer adipiscing elit Nam cursus Morbi ut mi Nullam enim leo egestas id condimentum at</p>
  <span class="read-more">READ MORE</span>
</article>

<div class="section-tab tab-teal" style="left:199px;top:1075px;width:514px"><span>BEST FOR FEATURES</span></div>
<article class="card feature-row" style="left:204px;top:1123px;width:500px">
  <div class="photo" style="flex:0 0 143px;height:85px;background:linear-gradient(135deg,#8a6a4e,#3b3028)" role="img" aria-label="Business team standing together"></div>
  <div><h3>Etiam eu urna Sed porta Suspendisse</h3>
  <p>consectetuer adipiscing elit Nam cursus Morbi ut mi Nullam enim leo egestas id condimentum at Duis quam Nam eget lacus Aliquam erat volutpat</p>
  <span class="read-more">READ MORE</span></div>
</article>
<article class="card feature-row" style="left:204px;top:1225px;width:500px">
  <div class="photo" style="flex:0 0 143px;height:84px;background:linear-gradient(135deg,#c8ced6,#34414f)" role="img" aria-label="Handshake between two business people"></div>
  <div><h3>Etiam eu urna Sed porta Suspendisse</h3>
  <p>consectetuer adipiscing elit Nam cursus Morbi ut mi Nullam enim leo egestas id condimentum at Duis quam Nam eget lacus Aliquam erat volutpat</p>
  <span class="read-more">READ MORE</span></div>
</article>

<div class="section-tab tab-blue" style="left:199px;top:1341px;width:514px"><span>BEST FOR DEVICE</span></div>
<article class="card" style="left:204px;top:1391px;width:162px">
  <div class="photo" style="height:85px;background:linear-gradient(135deg,#9aa3ab,#3a4047)" role="img" aria-label="Businessman in a city street"></div>
  <h4>Sed porta Suspendisse</h4><p>consectetuer adipiscing elit Nam cursus Morbi ut mi Nullam</p><time>01 DECEMBER 2015</time>
</article>
<article class="card" style="left:377px;top:1391px;width:162px">
  <div class="photo" style="height:85px;background:linear-gradient(135deg,#6fb3e0,#2c4a68)" role="img" aria-label="Two businessmen talking outdoors"></div>
  <h4>Sed porta Suspendisse</h4><p>consectetuer adipiscing elit Nam cursus Morbi ut mi Nullam</p><time>01 DECEMBER 2015</time>
</article>
<article class="card" style="left:548px;top:1391px;width:162px">
  <div class="photo" style="height:85px;background:linear-gradient(135deg,#e9ebef,#9a93b0)" role="img" aria-label="Colleagues working at a laptop"></div>
  <h4>Sed porta Suspendisse</h4><p>consectetuer adipiscing elit Nam cursus Morbi ut mi Nullam</p><time>01 DECEMBER 2015</time>
</article>

<div class="section-tab tab-teal" style="left:199px;top:1588px;width:514px"><span>LATEST REVIEWS</span></div>
<article class="card" style="left:202px;top:1636px;width:248px">
  <div class="photo" style="height:146px;background:linear-gradient(135deg,#3d4a55,#b08a6c)" role="img" aria-label="Woman looking at her phone"></div>
  <h3>Etiam eu urna Sed porta Suspendisse</h3>
  <p>consectetuer adipiscing elit Nam cursus Morbi ut mi Nullam enim leo egestas id condimentum at</p>
  <span class="read-more">READ MORE</span>
</article>
<article class="card" style="left:467px;top:1636px;width:248px">
  <div class="photo" style="height:146px;background:linear-gradient(135deg,#c7c3be,#f2f2f2)" role="img" aria-label="Person using a calculator at a desk"></div>
  <h3>Pellentesque rutrum males</h3>
  <p>consectetuer adipiscing elit Nam cursus Morbi ut mi Nullam enim leo egestas id condimentum at</p>
  <span class="read-more">READ MORE</span>
</article>

<div class="section-tab tab-blue" style="left:199px;top:1907px;width:514px"><span>LATEST ARTICLES</span></div>
<article class="card" style="left:204px;top:1955px;width:162px">
  <div class="photo" style="height:85px;background:linear-gradient(135deg,#8fd0e6,#3d8fb5)" role="img" aria-label="Illustration of cloud technology"></div>
  <h4>Sed porta Suspendisse</h4><p>consectetuer adipiscing elit Nam cursus Morbi ut mi Nullam</p><time>01 DECEMBER 2015</time>
</article>
<article class="card" style="left:377px;top:1955px;width:162px">
  <div class="photo" style="height:85px;background:linear-gradient(135deg,#e8e4da,#c9a25c)" role="img" aria-label="Illustration of social media speech bubbles"></div>
  <h4>Sed porta Suspendisse</h4><p>consectetuer adipiscing elit Nam cursus Morbi ut mi Nullam</p><time>01 DECEMBER 2015</time>
</article>
<article class="card" style="left:548px;top:1955px;width:162px">
  <div class="photo" style="height:85px;background:linear-gradient(135deg,#2f4552,#5f7a86)" role="img" aria-label="Chalkboard covered with idea sketches"></div>
  <h4>Sed porta Suspendisse</h4><p>consectetuer adipiscing elit Nam cursus Morbi ut mi Nullam</p><time>01 DECEMBER 2015</time>
</article>

<!-- right column -->
<div class="section-tab tab-teal" style="left:750px;top:466px;width:248px"><span>LATEST BLOG POSTS</span></div>
<article class="card post" style="left:750px;top:513px;width:248px">
  <div class="photo" style="height:147px;background:linear-gradient(#4f7fb8,#2c3e5e 60%,#d99a55)" role="img" aria-label="Wide view of a city at twilight"></div>
  <h4>Lorem ipsum dolor sit amet</h4>
  <p>consectetuer adipiscing elit Nam cursus Morbi ut mi Nullam enim leo egestas id condimentum at laoreet mattis Morbi diam mauris viverra in gravida eu mattis in ante Morbi eget arcu Morbi porta libero id ullamcorper nonum</p>
  <time>25 NOVEMBER 2015</time>
</article>
<article class="card post" style="left:750px;top:799px;width:248px">
  <div class="photo" style="height:147px;background:linear-gradient(#0b1a3c,#1d4f9a 70%,#8fc3ee)" role="img" aria-label="Planet Earth seen from space"></div>
  <h4>Lorem ipsum dolor sit amet</h4>
  <p>consectetuer adipiscing elit Nam cursus Morbi ut mi Nullam enim leo egestas id condimentum at laoreet mattis Morbi diam mauris viverra in gravida eu mattis in</p>
  <time>25 NOVEMBER 2015</time>
</article>
<article class="card post" style="left:750px;top:1068px;width:248px">
  <div class="photo" style="height:147px;background:linear-gradient(135deg,#f1f1f1,#c7c0b8)" role="img" aria-label="Smiling businesswoman in an office"></div>
  <h4>Lorem ipsum dolor sit amet</h4>
  <p>consectetuer adipiscing elit Nam cursus Morbi ut mi Nullam enim leo egestas id condimentum at la</p>
  <time>25 NOVEMBER 2015</time>
</article>
<article class="card post" style="left:750px;top:1329px;width:248px">
  <div class="photo" style="height:147px;background:linear-gradient(135deg,#a9c6e2,#7c8fa3)" role="img" aria-label="Photographer with a camera over a city"></div>
  <h4>Lorem ipsum dolor sit amet</h4>
  <p>consectetuer adipiscing elit Nam cursus Morbi ut mi Nullam enim leo egestas id condimentum at laoreet mattis Morbi diam mauris viverra in gravida eu mattis in ante Morbi eget arcu Morbi porta libero id ullamcorper nonum</p>
  <time>25 NOVEMBER 2015</time>
</article>
<article class="card post" style="left:750px;top:1621px;width:248px">
  <div class="photo" style="height:147px;background:linear-gradient(135deg,#d8d6d2,#8e8a84)" role="img" aria-label="Woman with a colourful umbrella on a bridge"></div>
  <h4>Lorem ipsum dolor sit amet</h4>
  <p>consectetuer adipiscing elit Nam cursus Morbi ut mi Nullam enim leo egestas id condimentum at laoreet mattis Morbi diam mauris viverra in gravida eu mattis in</p>
  <time>25 NOVEMBER 2015</time>
</article>
<article class="card post" style="left:750px;top:1896px;width:248px">
  <div class="photo" style="height:147px;background:linear-gradient(135deg,#9a9a9a,#2a2a2a)" role="img" aria-label="Man in sunglasses and a suit, black and white"></div>
  <h4>Lorem ipsum dolor sit amet</h4>
  <p>consectetuer adipiscing elit Nam cursus Morbi ut mi Nullam enim leo egestas id condimentum at la</p>
  <time>25 NOVEMBER 2015</time>
</article>

<footer class="site-footer">
  <nav class="footer-nav">
    <a href="#">HOME</a><a href="#">ABOUT</a><a href="#">ARTICLES</a><a href="#">NEWS</a><a href="#">FEATURES</a><a href="#">DEVICE</a><a href="#">REVIEWS</a><a href="#">GUIDES</a><a href="#">CONTACT</a>
  </nav>
  <div class="copyright">© 2015 Company Name &nbsp;All right reserved &nbsp;Term of Use</div>
  <div class="social" aria-label="Social links"><span></span><span></span><span></span><span></span></div>
</footer>

</body>
</html>
```